Newsletter template

I am looking for 2 newsletter templates. My website is in Wordpress and I want to use in mailchimp for lists.

One newsletter is for local clients of design remodeling firm to be sent monthly

Second newsletter is for web store offerings to be sent weekly.

Target Market(s)

Luxury home and leisure

Industry/Entity Type

Store

Requirements
Must have
• Use logos and colors to seamlessly integrate with website,

```html
<!DOCTYPE html>
<html lang="en">
<head>
<meta charset="utf-8">
<title>Corra Lane Fine Living – Newsletter</title>
<link href="https://fonts.googleapis.com/css2?family=Open+Sans:ital,wght@0,300;0,400;0,600;1,400;1,600&family=Gelasio:wght@400&display=swap" rel="stylesheet">
<style>
  :root {
    --cyan: #0e9cc0;
    --cyan-light: #18b8d8;
    --lime: #d8dc1a;
    --gold: #a9a41a;
    --ink: #3c3c3c;
    --body: #5a5a5a;
    --muted: #7a7a7a;
    --rule: #bdbdbd;
    --frame: #dcdcdc;
    --footer: #f1f1f1;
    --paper: #ffffff;
    --tag: #e2c233;
  }
  * { box-sizing: border-box; margin: 0; padding: 0; }
  html, body { width: 875px; height: 1200px; overflow: hidden; background: var(--paper); }
  body { position: relative; font-family: "Open Sans", Arial, sans-serif; color: var(--body); }
  .top-rule { position: absolute; left: 0; top: 0; width: 875px; height: 5px; background: #e9e9e9; }

  .brand { position: absolute; left: 0; top: 38px; width: 875px; text-align: center;
    font-family: "Open Sans", Arial, sans-serif; font-weight: 600; font-size: 24px; color: var(--cyan); letter-spacing: 0.5px; }
  .social { position: absolute; left: 753px; top: 61px; display: flex; gap: 6px; }
  .social span { width: 18px; height: 18px; display: block; border-radius: 2px; }
  .social .s1 { background: #3b5a9a; }
  .social .s2 { background: #3fb2e6; }
  .social .s3 { background: #1a70ad; }

  .hero { position: absolute; left: 44px; top: 94px; width: 787px; height: 290px; box-shadow: 0 2px 5px rgba(0,0,0,0.25); overflow: hidden; }
  .hero svg { position: absolute; left: 0; top: 0; }
  .hero-copy { position: absolute; left: 570px; top: 72px; width: 215px; color: #fff; }
  .hero-copy h1 { font-weight: 400; font-size: 21px; line-height: 26px; letter-spacing: -0.2px; }
  .hero-copy h2 { font-weight: 400; font-size: 15px; line-height: 22px; margin-bottom: 6px; }
  .hero-copy p { font-size: 9.6px; line-height: 17px; }

  .intro { position: absolute; left: 43px; top: 404px; width: 550px; }
  .intro h2 { font-weight: 400; font-size: 21px; color: var(--ink); line-height: 32px; margin-bottom: 4px; }
  .intro p { font-size: 9.4px; line-height: 15.5px; }

  .section-title { position: absolute; left: 44px; top: 517px; font-weight: 400; font-size: 18px; color: var(--cyan); }

  .item { position: absolute; left: 44px; width: 548px; }
  .item-photo { position: absolute; left: 0; top: 0; width: 112px; height: 91px; border: 1px solid var(--frame); }
  .item-photo .fill { position: absolute; inset: 3px; }
  .tag { position: absolute; left: 4px; top: 7px; background: var(--tag); color: #fff; font-size: 7.5px; font-weight: 600; padding: 2px 5px; }
  .item-body { position: absolute; left: 123px; top: 0; width: 425px; }
  .item-body h3 { font-family: "Gelasio", Georgia, serif; font-weight: 400; font-size: 15px; color: var(--gold); line-height: 20px; margin-bottom: 3px; }
  .item-body p { font-size: 9.2px; line-height: 15.4px; color: var(--muted); }
  .more { display: block; margin-top: 5px; font-style: italic; font-weight: 600; font-size: 9.2px; color: #555; }
  .divider { position: absolute; left: 44px; width: 540px; border-top: 1px dotted #9a9a9a; }

  .sidebar { position: absolute; left: 611px; top: 402px; width: 221px; height: 682px; border: 1px solid var(--frame); border-radius: 3px; }
  .side-card { position: absolute; left: 15px; width: 192px; }
  .side-photo { width: 192px; height: 96px; border: 1px solid var(--frame); border-radius: 3px; overflow: hidden; }
  .side-photo .fill { width: 100%; height: 100%; }
  .side-card h4 { font-weight: 400; font-size: 12.5px; color: var(--cyan); margin-top: 6px; line-height: 16px; }
  .side-card p { font-size: 8.8px; line-height: 15.2px; color: var(--muted); margin-top: 1px; }

  .footer { position: absolute; left: 0; top: 1146px; width: 875px; height: 54px; background: var(--footer); border-top: 2px solid #e6e6e6; }
  .footer p { position: absolute; left: 47px; top: 18px; font-size: 9.4px; color: var(--muted); }
</style>
</head>
<body>
  <div class="top-rule"></div>

  <header>
    <div class="brand">Corra Lane Fine Living</div>
    <div class="social" aria-label="Social links">
      <span class="s1"></span><span class="s2"></span><span class="s3"></span>
    </div>
  </header>

  <section class="hero">
    <svg width="787" height="290" viewBox="0 0 787 290">
      <defs>
        <linearGradient id="kitchen" x1="0" y1="0" x2="1" y2="1">
          <stop offset="0" stop-color="#d9d3cc"/>
          <stop offset="0.45" stop-color="#b9aea6"/>
          <stop offset="1" stop-color="#2a2524"/>
        </linearGradient>
        <linearGradient id="panel" x1="0" y1="0" x2="1" y2="1">
          <stop offset="0" stop-color="#1cbfdc"/>
          <stop offset="1" stop-color="#0a95bb"/>
        </linearGradient>
      </defs>
      <rect width="787" height="290" fill="url(#kitchen)" role="img" aria-label="Modern kitchen interior with red cabinets and a round white dining table"/>
      <path d="M575 0 C548 120 510 230 385 290 L787 290 L787 0 Z" fill="var(--lime)"/>
      <path d="M585 0 C560 125 520 235 405 290 L787 290 L787 0 Z" fill="url(#panel)"/>
      <rect x="600" y="6" width="180" height="278" fill="#ffffff" opacity="0.05"/>
    </svg>
    <div class="hero-copy">
      <h1>PELLENTESQUE FAUCIB</h1>
      <h2>QUISQUE DIGNISSIM CONGUE</h2>
      <p>Maecenas at justo id velit placerat molestie Donec dictum lectus non odio Cras a ante vitae enim iaculis aliquam Mauris nunc quam venenatis nec euismod</p>
    </div>
  </section>

  <section class="intro">
    <h2>Phasellus felis dolor scelerisque a tempus eget</h2>
    <p>Maecenas at justo id velit placerat molestie. Donec dictum lectus non odio. Cras a ante vitae enim iaculis aliquam. Mauris nunc quam, venenatis nec, euismod sit amet, egestas placerat, est. Pellentesque habitant morbi tristique senectus et netus et malesuada fames ac turpis egestas. Cras id elit. Integer quis urna. Ut ante enim, dapibus malesuada, fringilla eu, condimentum quis, tellus. Aenean porttitor eros vel dolor. Donec convallis pede venenatis nibh.</p>
  </section>

  <h2 class="section-title">Product Newsletters</h2>

  <article class="item" style="top:550px;">
    <div class="item-photo"><div class="fill" role="img" aria-label="Silver sculptural candle holder" style="background:linear-gradient(135deg,#f4f4f4,#9a9a9a 55%,#e8e8e8);"></div></div>
    <div class="item-body">
      <h3>Maecenas at justo id velit</h3>
      <p>molestie. Donec dictum lectus non odio. Cras a ante vitae enim iaculis aliquam. Mauris nunc quam, venenatis nec, euismod sit amet, egestas placerat, est. Pellentesque habitant morbi tristique senectus et netus et malesuada fames ac turpis egestas. Cras id elit. Integer quis urna. Ut ante enim, dapibus malesuada, fringilla eu, Ut ante enim, dapibus malesuada,</p>
      <span class="more">Click here to read more</span>
    </div>
  </article>
  <div class="divider" style="top:668px;"></div>

  <article class="item" style="top:686px;">
    <div class="item-photo" style="height:91px;"><div class="fill" role="img" aria-label="Red metal watering can" style="background:radial-gradient(circle at 60% 55%,#d8322a,#b82a22 35%,#f6f2f0 70%);"></div><span class="tag">NEW</span></div>
    <div class="item-body">
      <h3>Vivamus porttitor neque</h3>
      <p>Phasellus felis dolor, scelerisque a, tempus eget, lobortis id, libero. Aliquam nec erat at purus cursus interdum. Vestibulum ligula augue, bibendum accumsan, vestibulum ut, commodo a, mi. Morbi ornare gravida elit. Integer congue, augue et malesuada iaculis, ipsum dui aliquet felis, at cursus magna nisl nec elit. Vestibulum gravida. Praesent elementum elit at tellus. Malesuada nec, ultricies sit amet, porttitor mattis, enim. In massa libero, interdum nec, interdum vel, blandit sed, nulla. In ullamcorper, est eget tempor cursus, neque mi consectetuer mi</p>
      <span class="more">Click here to read more</span>
    </div>
  </article>
  <div class="divider" style="top:830px;"></div>

  <article class="item" style="top:846px;">
    <div class="item-photo" style="border:none;"><div class="fill" role="img" aria-label="Cream towel on a wall mounted towel bar" style="inset:0;background:radial-gradient(circle at 45% 55%,#efe6cf,#c7b58a 40%,#8f7a4e);"></div><span class="tag">NEW</span></div>
    <div class="item-body">
      <h3>Curabitur tristique condimentum</h3>
      <p>molestie. Donec dictum lectus non odio. Cras a ante vitae enim iaculis aliquam. Mauris nunc quam, venenatis nec, euismod sit amet, egestas placerat, est. Pellentesque habitant morbi tristique senectus et netus et malesuada fames ac turpis egestas. Cras id elit. Integer quis urna. Ut ante enim, dapibus malesuada, fringilla eu, Ut ante enim, dapibus malesuada, fringilla eu, condimentum quis, tellus. Aenean porttitor eros vel dolor.</p>
      <span class="more">Click here to read more</span>
    </div>
  </article>
  <div class="divider" style="top:974px;"></div>

  <article class="item" style="top:994px;">
    <div class="item-photo"><div class="fill" role="img" aria-label="Copper and pewter acorn shaped box" style="background:radial-gradient(circle at 50% 60%,#b9784a,#8a8a86 45%,#ffffff 72%);"></div></div>
    <div class="item-body">
      <h3>Mauris vel lacus vitae</h3>
      <p>molestie. Donec dictum lectus non odio. Cras a ante vitae enim iaculis aliquam. Mauris nunc quam, venenatis nec, euismod sit amet, egestas placerat, est. Pellentesque habitant morbi tristique senectus et netus et malesuada fames ac turpis egestas. Cras id elit. Integer quis urna. Ut ante enim, dapibus malesuada, fringilla eu, Ut ante enim, dapibus malesuada, fringilla eu, condimentum quis, tellus. Aenean porttitor eros vel dolor.</p>
      <span class="more">Click here to read more</span>
    </div>
  </article>

  <aside class="sidebar">
    <div class="side-card" style="top:13px;">
      <div class="side-photo"><div class="fill" role="img" aria-label="White dinnerware set with red lobster print" style="background:linear-gradient(120deg,#f1eeee,#d9584a 50%,#efe9e8);"></div></div>
      <h4>Nulla sit amet diam</h4>
      <p>velit placerat molestie Donec dictum lectus non odio Cras a ante vitae enim iaculis aliquam Mauris nunc quam venenatis nec euismod sit amet egestas placerat</p>
    </div>
    <div class="side-card" style="top:209px;">
      <div class="side-photo"><div class="fill" role="img" aria-label="Black quilted rolling cooler bag" style="background:radial-gradient(circle at 55% 65%,#2b2b2b,#4a4a4a 45%,#ffffff 75%);"></div></div>
      <h4>Quisque dignissim congue</h4>
      <p>velit placerat molestie Donec dictum lectus non odio Cras a ante vitae enim iaculis aliquam Mauris nunc quam venenatis nec euismod sit amet egestas placerat</p>
    </div>
    <div class="side-card" style="top:407px;">
      <div class="side-photo"><div class="fill" role="img" aria-label="Round charcoal grill with food tray" style="background:linear-gradient(135deg,#e9e9e9,#4a4a4a 40%,#1f1f1f 75%,#a0523c);"></div></div>
      <h4>Duis non nunc</h4>
      <p>Donec dictum lectus non odio. Cras a ante vitae enim iaculis aliquam. Mauris nunc quam, venenatis nec, euismod<br>sit amet, egestas placerat, est. Pellentesque habitant morbi tristique senectus et netus et malesuada<br>fames ac turpis egestas. Cras id elit. Integer quis urna. Ut ante enim</p>
    </div>
  </aside>

  <footer class="footer">
    <p>Copyright © 2014 Company Name.&nbsp; All right reserved.</p>
  </footer>
</body>
</html>
```